Tend Your Harvest - Keep your Bloom - The freedom to choose and participate in your own path to hea

I have a logo that needs to be turned into a large banner for my website. I want to keep the same font in the uploaded logo image. Now this image could stay at the top of the header kind of where it is now on the web site, It doesn't have to be the main thing on the page. I want this header to be artistic - alive, healthy, joyous - colorful banner that shows wellness, healing, vitality and hope.
If you had a chronic illness and came to my site what would you want to see? You'd want to feel empowered, enlightened, engaged, hopeful and feel the love, right?.
I look forward to getting your creative ideas and designs.

Target Market(s)

People struggling with illness who are looking for a better quality of life. We provide training and education on how to do that. Hope, happiness - healing - Vitality - whole natural foods - mediation - visualization - whole health.

Industry/Entity Type

Health And Wellness

Logo Text

Tend Your Harvest with the koru and with Marigold Thwaite (use the font on the uploaded file)

Requirements
Must have
• I've changed the photos in this order. You can pick up options here:
• https://www.filebarrow.example/s/x7pleqnrtwz2kdm/IMG_4402%20%20high%20resolution.jpg?dl=0
• https://www.filebarrow.example/s/m3bvohqyeuc8zta/IMG_4587%20high%20resolution.jpg?dl=0
• My original logo - Tend Your Harvest - Marigold Thwaite
• "Together we make tragic moments magic moments" Join us (sign up type button)
Nice to have
• Something stunningly simple, classy, inviting, where my message gets across.
• Here's a similar website to mine: http://dalvenhope.example
• I need a link to join up somewhere - with my quote.
• "My tragic moments have become magic moments" Join us (sign up type button)
Should not have
• I do not want other people in the header.
• No crunchy granola feel!
• This is gone mainstream now.

```html
<!DOCTYPE html>
<html lang="en">
<head>
<meta charset="utf-8">
<title>Tend Your Harvest – Header Banner</title>
<link rel="stylesheet" href="https://fonts.googleapis.com/css2?family=Open+Sans:wght@300;400;600&display=swap">
<style>
  :root {
    --teal-deep: #4f9597;
    --teal-mid: #6eaaa9;
    --teal-light: #8cc0bd;
    --portrait-warm: #e6b99a;
    --portrait-hair: #d08a55;
    --portrait-shirt: #b9dcdf;
    --badge-top: #ffffff;
    --badge-bottom: #e3e8ea;
    --badge-edge: #c9d3d6;
    --brand-teal: #5fb3b6;
    --accent-gold: #f2a81d;
    --tagline-white: #ffffff;
    --button-text: #2f6f71;
  }
  * { box-sizing: border-box; margin: 0; padding: 0; }
  html, body { width: 1200px; height: 440px; overflow: hidden; }
  body { font-family: "Open Sans", Arial, sans-serif; }

  .banner {
    position: relative;
    width: 1200px;
    height: 440px;
    overflow: hidden;
    background:
      radial-gradient(ellipse 520px 380px at 620px 200px, rgba(255,255,255,0.18), transparent 70%),
      linear-gradient(90deg, var(--teal-deep) 0%, var(--teal-mid) 45%, var(--teal-light) 75%, var(--teal-mid) 100%);
  }

  .portrait {
    position: absolute;
    left: 330px;
    top: 0;
    width: 600px;
    height: 440px;
    background:
      radial-gradient(ellipse 150px 190px at 300px 210px, var(--portrait-warm) 0%, rgba(230,185,154,0.6) 55%, transparent 80%),
      radial-gradient(ellipse 260px 260px at 300px 220px, rgba(208,138,85,0.55) 0%, transparent 75%),
      radial-gradient(ellipse 240px 90px at 300px 430px, var(--portrait-shirt) 0%, transparent 80%);
    filter: blur(4px);
  }

  .brand-badge {
    position: absolute;
    left: 0;
    top: 160px;
    width: 410px;
    height: 116px;
    padding: 12px 18px 0 18px;
    background: linear-gradient(180deg, var(--badge-top) 0%, var(--badge-bottom) 100%);
    border: 1px solid var(--badge-edge);
    border-left: none;
    border-radius: 0 6px 6px 0;
    box-shadow: 0 2px 6px rgba(0,0,0,0.12);
    color: var(--brand-teal);
    font-weight: 300;
  }
  .brand-name {
    display: flex;
    align-items: center;
    gap: 10px;
    font-size: 34px;
    line-height: 44px;
    white-space: nowrap;
  }
  .brand-dot {
    width: 20px;
    height: 20px;
    border-radius: 50%;
    background: var(--brand-teal);
    flex: none;
  }
  .brand-owner {
    margin-left: 30px;
    margin-top: 6px;
    font-size: 29px;
    line-height: 38px;
    white-space: nowrap;
  }

  .join {
    position: absolute;
    left: 20px;
    top: 306px;
    width: 320px;
    color: var(--tagline-white);
  }
  .join-quote {
    font-size: 17px;
    font-weight: 400;
    font-style: normal;
    line-height: 24px;
  }
  .join-button {
    display: inline-block;
    margin-top: 12px;
    padding: 8px 26px;
    border-radius: 4px;
    background: var(--accent-gold);
    color: var(--tagline-white);
    font-size: 17px;
    font-weight: 600;
    text-decoration: none;
  }

  .tagline {
    position: absolute;
    left: 918px;
    top: 118px;
    padding-left: 14px;
    border-left: 7px solid var(--accent-gold);
    list-style: none;
    color: var(--tagline-white);
    font-weight: 600;
    font-size: 64px;
    line-height: 77px;
    white-space: nowrap;
  }
</style>
</head>
<body>
  <header class="banner">
    <div class="portrait" role="img" aria-label="Portrait of Marigold Thwaite smiling, soft warm light"></div>

    <div class="brand-badge">
      <div class="brand-name"><span class="brand-dot"></span>Tend Your Harvest</div>
      <div class="brand-owner">Marigold Thwaite</div>
    </div>

    <div class="join">
      <p class="join-quote">“Together we make tragic moments magic moments”</p>
      <a class="join-button" href="#join">Join us</a>
    </div>

    <ul class="tagline">
      <li>Inspire</li>
      <li>Inform</li>
      <li>Ignite</li>
    </ul>
  </header>
</body>
</html>
```